pathology learning flashcard template graphic design .

Creative designs for 2 sides of the flashcards to include colorful sectioning and font sizes that will make it easy to use in studying.

```html
<!DOCTYPE html>
<html lang="en">
<head>
<meta charset="utf-8">
<title>Pathology Flashcard – Achalasia</title>
<link href="https://fonts.googleapis.com/css2?family=Amaranth:ital,wght@0,400;0,700;1,400;1,700&family=Carlito:ital,wght@0,400;0,700;1,400;1,700&display=swap" rel="stylesheet">
<style>
:root{
  --brand-blue:#0b68b1;
  --pale-blue:#d3eaf9;
  --ink:#111;
  --frame:#555;
  --white:#fff;
}
*{box-sizing:border-box;margin:0;padding:0}
html,body{width:863px;height:1200px;overflow:hidden;background:var(--white)}
body{position:relative;font-family:"Carlito",sans-serif;color:var(--ink)}
.cut-frame{position:absolute;left:0;width:863px;border:1px solid var(--frame)}
.cut-frame.front{top:0;height:592px;border-top:none}
.cut-frame.back{top:604px;height:596px;border-bottom:none}

/* FRONT */
.card-front{position:absolute;left:22px;top:21px;width:819px;height:549px;border:3.5px solid var(--ink);border-radius:34px;overflow:hidden;background:var(--white)}
.front-side{position:absolute;left:0;top:0;width:345px;height:100%}
.category{position:absolute;left:0;width:345px;top:18px;text-align:center;font-family:"Amaranth",sans-serif;font-weight:700;font-size:37px;color:var(--brand-blue)}
.category-art{position:absolute;left:77px;top:68px;width:198px;height:198px;border-radius:50%;border:3px solid var(--brand-blue);background:radial-gradient(circle at 50% 45%,#f4f4f4 0 45%,#dcecf8 46%)}
.case-band{position:absolute;left:4px;top:283px;width:341px;height:44px;background:var(--pale-blue);font-family:"Amaranth",sans-serif;font-weight:700;font-style:italic;font-size:25.5px;line-height:44px;text-align:center}
.sex-icon{position:absolute;left:91px;top:337px}
.age{position:absolute;left:0;width:345px;top:506px;text-align:center;font-family:"Amaranth",sans-serif;font-weight:700;font-size:22px;color:var(--brand-blue)}
.question-panel{position:absolute;left:345px;top:0;right:0;bottom:0;background:var(--pale-blue);padding:18px 15px 0 17px}
.question{font-size:21.6px;line-height:26.3px;text-align:justify}
.options{list-style:none;position:absolute;left:17px;top:418px;font-size:21.6px;line-height:27.5px}

/* NOTE */
.note{position:absolute;left:56px;width:751px;top:576px;text-align:center;background:var(--white);font-family:"Amaranth",sans-serif;font-weight:700;font-size:18.5px;line-height:21px}

/* BACK */
.card-back{position:absolute;left:22px;top:626px;width:819px;height:549px;border:4px solid var(--brand-blue);border-radius:34px;overflow:hidden;background:var(--white)}
.topic{position:absolute;left:18px;top:14px;font-family:"Amaranth",sans-serif;font-weight:700;font-style:italic;font-size:37px;color:var(--brand-blue)}
.column{position:absolute;top:70px;width:379px;font-size:16.2px;line-height:19.1px;text-align:justify}
.column.left{left:14px}
.column.right{left:423px;top:89px}
.column h3{font-family:"Amaranth",sans-serif;font-weight:700;font-style:italic;font-size:16.5px;line-height:19px}
.column p{margin-bottom:19px}
.answer-band{position:absolute;left:0;right:0;top:353px;bottom:0;background:var(--pale-blue);padding:14px 15px 0 14px}
.answer-band h3{font-family:"Amaranth",sans-serif;font-weight:700;font-style:italic;font-size:16.5px;line-height:19px}
.answer-band p{font-style:italic;font-size:16.2px;line-height:19.2px;text-align:justify;letter-spacing:.2px}
.sources{position:absolute;left:14px;top:503px;font-size:13px}
.card-number{position:absolute;left:748px;top:482px;width:67px;height:67px;border-radius:50%;border:3.5px solid var(--ink);background:var(--white);font-weight:700;font-size:42px;line-height:60px;text-align:center}
</style>
</head>
<body>
<div class="cut-frame front"></div>
<div class="cut-frame back"></div>

<section class="card-front">
  <div class="front-side">
    <h1 class="category">Gastrointestinal</h1>
    <div class="category-art" role="img" aria-label="Illustration of a stomach containing assorted microbes"></div>
    <div class="case-band">Pathology Case ID 0001</div>
    <svg class="sex-icon" width="168" height="168" viewBox="0 0 168 168" aria-label="Male symbol">
      <circle cx="84" cy="84" r="84" fill="var(--brand-blue)"/>
      <circle cx="68" cy="100" r="34" fill="none" stroke="#fff" stroke-width="10"/>
      <path d="M93 75 L130 38" stroke="#fff" stroke-width="10"/>
      <path d="M96 26 H140 V70 H130 V36 H96 Z" fill="#fff"/>
    </svg>
    <div class="age">Age: 50 years</div>
  </div>
  <div class="question-panel">
    <p class="question">50-year-old woman comes to the clinic because she has difficulty swallowing for the past few months. She says symptoms have been worsening. She also complains of cough, <em>mostly at night and in fear of choking, has stopped eating many foods,</em> losing about 12 lbs in the past 3 months. Past medical history is unremarkable. Vital signs are normal and physical exam is unremarkable. Chest x-ray with demonstrates an <em>air-fluid level, while manometry shows absent relaxation of the</em> lower esophageal sphincter during swallow-ing. What is the most likely diagnosis?</p>
    <ul class="options">
      <li>A) GERD</li>
      <li>B) Barret Esophagus</li>
      <li>C) Achalasia</li>
      <li><em>D) Eosinophilic esophagitis</em></li>
    </ul>
  </div>
</section>

<p class="note">Fonts changed to Brindle and Corvale / Corvale Italic and not sure if the<br>gender symbol instead of a person’s face simplifies matters</p>

<section class="card-back">
  <h2 class="topic">Achalasia</h2>
  <div class="column left">
    <h3>Definition:</h3>
    <p><em>Motility disorder where esophageal relaxation is impaired in the lower esophageal</em> sphincter (LES).</p>
    <h3>Etiology/Pathology:</h3>
    <p><em>Destruction of inhibitory neurons in the Auerbach plexus.</em> Loss of peristalsis in the lower esophageal sphincter (lower two thirds of the esophagus).</p>
    <h3>P/E and Symptoms:</h3>
    <p>Dysphagia that is progressive, regurgitation, weight-loss, dry cough, chest pain, GERD, esophageal perforation, squamous cell carcinoma, aspiration pneumonia.</p>
  </div>
  <div class="column right">
    <p><em>Barium swallow will show ‘bird’s beak’ and esophageal dilation. Manometry will present with increased resting lower esophageal</em> sphincter pressure. <em>Endoscopy will usually present with normal mucosa and LES dilation, and in some cases residual material such as undigested food particles may be present.</em></p>
    <h3>Rx:</h3>
    <p><em>First line of treatment are nitrates, calcium channel blockers, and Botulinum toxin injection in the LES. Long term management options include esophageal dilation with pneumatic balloon and myotomy.</em></p>
  </div>
  <div class="answer-band">
    <h3>C-Achalasia</h3>
    <p>Symptoms and studies suggestive of achalasia. Patient’s manometry presents with no relaxation of the lower esophageal sphincter during swallowing. Patient also complains of dysphagia and is unable to swallow properly, leading to weight loss. Patient has no past infection or inflammation, ruling out eosinophilic esophagitis. Patient does not have GERD, eliminating the possibility of Barrett esophagus, in which at least 5 years of acid reflux are beforehand to develop columnar metaplasia.</p>
  </div>
  <p class="sources">Sources: Harlow’s Drug Guide; Pembry Pocket Formulary; Medivra.com; Clinoptica.com</p>
  <div class="card-number">1</div>
</section>
</body>
</html>
```